Church needs an introductory/informative postcard

We are looking for a postcard that would introduce our church along with having our programing information. We need it to be in Spanish, I can provide the necessary translation. Please provide us with ideas for a tag line that invites people to come check us out. We can provide a bible scripture if necessary, but would like something short that projects interest and confidence. We have a logo that we would like incorporated.

Target Market(s)

Hispanic

Industry/Entity Type

Religious

Requirements
Must have
• Colorful to coordinate with our logo so it flows well
• Have an tag line that invites people to our church
Nice to have
• have a modern feel
• if needed we can provide some pictures of our building
Should not have
• Pictures of people

```html
<!DOCTYPE html>
<html lang="es">
<head>
<meta charset="utf-8">
<title>Iglesia de Dios Betania — Postal</title>
<link rel="stylesheet" href="https://fonts.googleapis.com/css2?family=Cinzel:wght@400;700&family=Open+Sans:ital,wght@0,400;0,600;0,700;1,400&display=swap">
<style>
  :root {
    --canvas: #e4e4e4;
    --paper: #ffffff;
    --ink: #2f2f2f;
    --ink-soft: #4a4a4a;
    --purple: #6a3f97;
    --orange: #f15a24;
    --orange-light: #f7931e;
    --green: #5aa02c;
    --green-dark: #3f7d1c;
    --blue: #1d8fd0;
    --blue-dark: #1a6fae;
    --rule: #8a8a8a;
  }
  * { box-sizing: border-box; margin: 0; padding: 0; }
  html, body {
    width: 906px; height: 1200px; overflow: hidden;
    background: var(--canvas);
    font-family: "Open Sans", Arial, sans-serif;
    color: var(--ink);
  }
  .canvas { position: relative; width: 906px; height: 1200px; }

  .postcard {
    position: absolute;
    width: 680px; height: 510px;
    background: var(--paper);
    overflow: hidden;
    box-shadow: 0 4px 14px rgba(0,0,0,.18);
  }
  .postcard--front { left: 40px; top: 60px; }
  .postcard--back  { left: 186px; top: 630px; }
  .postcard__art { position: absolute; inset: 0; width: 680px; height: 510px; }

  /* brand name stand-in */
  .brand {
    position: absolute;
    display: flex; flex-direction: column; align-items: center; gap: 8px;
  }
  .brand__dot {
    width: 38px; height: 38px; border-radius: 50%;
    background: var(--orange);
  }
  .brand__name {
    font-family: "Open Sans", Arial, sans-serif;
    font-weight: 600;
    color: var(--purple);
    letter-spacing: 1px;
  }
  .postcard--front .brand { left: 38px; top: 72px; }
  .postcard--front .brand__name { font-size: 30px; }
  .postcard--back .brand { left: 420px; top: 28px; gap: 6px; }
  .postcard--back .brand__dot { width: 30px; height: 30px; }
  .postcard--back .brand__name { font-size: 22px; }

  /* front */
  .tagline {
    position: absolute; left: 0; right: 0; top: 372px;
    text-align: center;
    font-family: "Cinzel", Georgia, serif;
    font-weight: 400;
    font-size: 50px;
    line-height: 56px;
    letter-spacing: 2px;
    color: var(--ink);
    padding-left: 40px;
  }
  .scripture {
    position: absolute; left: 100px; right: 40px; top: 428px;
    text-align: center;
    font-style: italic;
    font-size: 12.5px;
    line-height: 17px;
    color: var(--ink-soft);
  }
  .web {
    position: absolute;
    font-size: 13px;
    color: #fff;
  }
  .postcard--front .web { left: 26px; top: 483px; }

  /* back */
  .schedule {
    position: absolute; left: 20px; top: 250px;
    display: grid; grid-template-columns: 150px 120px; row-gap: 6px;
    align-items: center;
  }
  .schedule__day {
    font-family: "Cinzel", Georgia, serif;
    font-weight: 700; font-size: 18px; line-height: 24px; color: var(--ink);
  }
  .schedule__time {
    background: linear-gradient(var(--green), var(--green-dark));
    color: #fff; font-size: 15px; text-align: center;
    border-radius: 11px; height: 22px; line-height: 22px;
  }
  .call {
    position: absolute; left: 60px; top: 340px;
    font-weight: 700; font-size: 17px; line-height: 22px; color: var(--green-dark);
  }
  .phone {
    position: absolute; left: 0; top: 366px; width: 300px; height: 32px;
    background: linear-gradient(90deg, var(--blue-dark), var(--blue));
    color: #fff; font-weight: 700; font-size: 22px; line-height: 32px;
    padding-left: 62px;
  }
  .address {
    position: absolute; left: 22px; top: 410px;
    display: flex; gap: 10px;
  }
  .address__icon { width: 18px; height: 18px; margin-top: 2px; }
  .address__text { font-size: 14px; line-height: 18px; color: var(--ink-soft); }
  .postcard--back .web { left: 26px; top: 478px; font-size: 12px; }

  .stamp {
    position: absolute; left: 566px; top: 24px; width: 84px; height: 96px;
    border: 3px dotted #9a9a9a; padding: 5px;
  }
  .stamp__inner { width: 100%; height: 100%; border: 2px solid #9a9a9a; }
  .mail-lines { position: absolute; left: 400px; top: 280px; width: 250px; }
  .mail-lines__rule { height: 1px; background: var(--rule); margin-bottom: 38px; }
</style>
</head>
<body>
<main class="canvas">

  <!-- Front of postcard -->
  <section class="postcard postcard--front" aria-label="Frente de la postal">
    <svg class="postcard__art" viewBox="0 0 680 510">
      <defs>
        <linearGradient id="frontSky" x1="0" y1="0" x2="1" y2="1">
          <stop offset="0" stop-color="#2f6fc4"/>
          <stop offset=".45" stop-color="#5c9be0"/>
          <stop offset=".75" stop-color="#a8523a"/>
          <stop offset="1" stop-color="#8a4a34"/>
        </linearGradient>
        <linearGradient id="frontStone" x1="0" y1="0" x2="0" y2="1">
          <stop offset="0" stop-color="#f4f4f4"/>
          <stop offset="1" stop-color="#dcdcdc"/>
        </linearGradient>
        <linearGradient id="frontStrip" x1="0" y1="0" x2="1" y2="0">
          <stop offset="0" stop-color="#f7931e"/>
          <stop offset="1" stop-color="#f15a24"/>
        </linearGradient>
      </defs>
      <rect width="680" height="510" fill="url(#frontStone)"/>
      <path d="M0,0 H300 C270,150 200,270 0,320 Z" fill="#ffffff"/>
      <path d="M250,0 H680 V290 C560,315 420,335 250,365 C160,380 80,390 0,395 V330 C190,290 270,160 250,0 Z" fill="#ffffff"/>
      <path role="img" aria-label="Fotografía de la fachada de ladrillo de la iglesia con su campanario blanco bajo un cielo azul"
            d="M282,0 H680 V282 C520,308 300,345 30,372 C180,300 290,170 282,0 Z"
            fill="url(#frontSky)"/>
      <path d="M262,0 C272,170 180,310 20,376" fill="none" stroke="var(--orange)" stroke-width="10"/>
      <path d="M246,0 C254,150 190,270 60,318" fill="none" stroke="var(--green)" stroke-width="5"/>
      <path d="M0,380 C200,350 420,320 680,284" fill="none" stroke="var(--green)" stroke-width="16"/>
      <path d="M0,398 C200,368 440,338 680,306" fill="none" stroke="var(--blue)" stroke-width="10"/>
      <path d="M0,474 H250 C275,474 290,495 300,510 H0 Z" fill="url(#frontStrip)"/>
    </svg>

    <div class="brand">
      <span class="brand__dot"></span>
      <span class="brand__name">BETANIA</span>
    </div>

    <h1 class="tagline">VEN A VER</h1>
    <p class="scripture">Porque tanto amó Dios al mundo, que dio a su Hijo unigénito, para que todos los que creen<br>en él no se pierdan, sino que tengan vida eterna.</p>
    <span class="web">www.iglesiabetania.org</span>
  </section>

  <!-- Back of postcard -->
  <section class="postcard postcard--back" aria-label="Reverso de la postal">
    <svg class="postcard__art" viewBox="0 0 680 510">
      <defs>
        <linearGradient id="backStone" x1="0" y1="0" x2="0" y2="1">
          <stop offset="0" stop-color="#f2f2f2"/>
          <stop offset="1" stop-color="#dedede"/>
        </linearGradient>
        <linearGradient id="backPhoto" x1="0" y1="0" x2="1" y2="1">
          <stop offset="0" stop-color="#6fa6de"/>
          <stop offset=".5" stop-color="#c8dcef"/>
          <stop offset=".8" stop-color="#a35a3c"/>
          <stop offset="1" stop-color="#9a9a90"/>
        </linearGradient>
        <linearGradient id="backStrip" x1="0" y1="0" x2="1" y2="0">
          <stop offset="0" stop-color="#f7931e"/>
          <stop offset="1" stop-color="#f15a24"/>
        </linearGradient>
      </defs>
      <path d="M0,0 H350 C400,150 390,340 320,510 H0 Z" fill="url(#backStone)"/>
      <path role="img" aria-label="Fotografía del edificio de la iglesia con campanario y estacionamiento"
            d="M0,0 H345 C360,60 366,120 364,170 C250,175 130,200 0,228 Z"
            fill="url(#backPhoto)"/>
      <path d="M0,236 C130,208 250,184 366,178" fill="none" stroke="var(--green)" stroke-width="6"/>
      <path d="M350,0 C400,150 390,340 320,510" fill="none" stroke="var(--orange)" stroke-width="10"/>
      <path d="M334,0 C380,150 372,330 306,510" fill="none" stroke="var(--green)" stroke-width="4"/>
      <path d="M0,472 H300 C310,480 312,490 310,500 H0 Z" fill="url(#backStrip)"/>
    </svg>

    <div class="schedule">
      <span class="schedule__day">DOMINGO</span><span class="schedule__time">10:00 am</span>
      <span class="schedule__day">LUNES</span><span class="schedule__time">7:00 pm</span>
      <span class="schedule__day">MIÉRCOLES</span><span class="schedule__time">7:00 pm</span>
    </div>

    <p class="call">Llámanos:</p>
    <p class="phone">555.010.2468</p>

    <div class="address">
      <svg class="address__icon" viewBox="0 0 20 20" aria-hidden="true">
        <path d="M10,2 L19,10 H16 V18 H12 V13 H8 V18 H4 V10 H1 Z" fill="var(--orange)"/>
      </svg>
      <p class="address__text">Iglesia de Dios Betania<br>2480 Alameda Ave.<br>Riverton, TX 75999</p>
    </div>

    <span class="web">www.iglesiabetania.org</span>

    <div class="brand">
      <span class="brand__dot"></span>
      <span class="brand__name">BETANIA</span>
    </div>

    <div class="stamp" aria-label="Espacio para sello"><div class="stamp__inner"></div></div>

    <div class="mail-lines" aria-label="Líneas para la dirección">
      <div class="mail-lines__rule"></div>
      <div class="mail-lines__rule"></div>
      <div class="mail-lines__rule"></div>
      <div class="mail-lines__rule"></div>
      <div class="mail-lines__rule"></div>
    </div>
  </section>

</main>
</body>
</html>
```